Norvale (PTY)LTD / Stationary design

Create proffesional stationary to match the logo design that was done by craft bureau.

we are looking for designs of letter heads, notepads, calendars, log books, receipt books, daily site diaries, banners and marketing materials. all the designs must be in line with the logo designs that was done previously by craft bureau and need to stay with the same theme as previously.

Target Market(s)

clients in the same industry, architects, engineers, developers

Contact Information for Business Card

all the normal details that is normally on a professional business card, name, title, email add, web address, City and country, contact numbers. one of the sides should have the logo on it.

Font styles to use
Serif
Sans Serif

Colors

Designer to choose colors to be used in the design.

Requirements
Must have
• must look very professional

```html
<!DOCTYPE html>
<html lang="en">
<head>
<meta charset="utf-8">
<title>Norvale (PTY)LTD — Letterhead</title>
<link rel="stylesheet" href="https://fonts.googleapis.com/css2?family=Mulish:wght@400;600;800&display=swap">
<style>
  :root {
    --backdrop: #d4d4d4;
    --paper: #f4f4f4;
    --paper-shade: #e2e2e2;
    --brand-blue: #2a8fd4;
    --brand-navy: #1c5ea6;
    --ink: #555b63;
  }
  * { margin: 0; padding: 0; box-sizing: border-box; }
  html, body {
    width: 1200px; height: 780px; overflow: hidden;
    background: var(--backdrop);
    font-family: "Mulish", sans-serif;
  }
  .letterhead {
    position: absolute; left: 338px; top: 20px;
    width: 523px; height: 740px;
    background: linear-gradient(160deg, var(--paper) 0%, var(--paper-shade) 100%);
    box-shadow: 0 6px 24px rgba(0,0,0,0.18);
  }
  .brand {
    position: absolute; left: 47px; top: 50px;
    display: flex; align-items: center; gap: 8px;
  }
  .brand-square {
    width: 22px; height: 22px; background: var(--brand-blue);
  }
  .brand-name {
    font-weight: 800; font-size: 32px; line-height: 1;
    color: var(--brand-blue); letter-spacing: -0.5px;
  }
  .footer-contact {
    position: absolute; left: 57px; top: 694px;
    display: flex; gap: 10px;
    font-size: 7px; line-height: 11px; color: var(--ink);
  }
  .contact-line { display: flex; align-items: center; gap: 5px; }
  .contact-line svg { width: 7px; height: 7px; fill: var(--brand-navy); }
  .web-band {
    position: absolute; left: 343px; top: 699px;
    display: flex; align-items: stretch; height: 12px;
  }
  .web-band .stripe { width: 4px; background: var(--brand-blue); margin-right: 2px; }
  .web-band .stripe:nth-child(3) { margin-right: 3px; }
  .web-band .url {
    width: 146px; background: var(--brand-navy); color: #fff;
    font-size: 7px; letter-spacing: 1px; line-height: 12px; padding-left: 17px;
    font-weight: 600;
  }
  .web-band .cap { width: 13px; background: var(--brand-blue); }
</style>
</head>
<body>
  <main class="letterhead">
    <header class="brand">
      <span class="brand-square"></span>
      <span class="brand-name">Norvale</span>
    </header>

    <footer>
      <div class="footer-contact">
        <address class="contact-address" style="font-style:normal">
          14 Harbour Lane, Quarry Park<br>
          Stonebridge, CA 45120
        </address>
        <div class="contact-channels">
          <div class="contact-line">
            <svg viewBox="0 0 10 10"><path d="M2 0.5 L3.8 2.6 L2.9 3.6 Q4 6 6.4 7.1 L7.4 6.2 L9.5 8 L8.3 9.5 Q4.5 9.3 2 6.8 Q0.2 4.5 0.5 1.7 Z"/></svg>
            <span>+27 21 555 0148</span>
          </div>
          <div class="contact-line">
            <svg viewBox="0 0 10 10"><path d="M0.5 2 H9.5 V8.5 H0.5 Z M1.2 2.6 L5 5.6 L8.8 2.6" fill="none" stroke="#1c5ea6" stroke-width="1.2"/></svg>
            <span>hello@norvale.co.za</span>
          </div>
        </div>
      </div>

      <div class="web-band">
        <span class="stripe"></span>
        <span class="stripe"></span>
        <span class="stripe"></span>
        <span class="url">www.norvale.co.za</span>
        <span class="cap"></span>
      </div>
    </footer>
  </main>
</body>
</html>
```